New Wedding Decor Web Design Project - GUARANTEED PAYMENT

We need to have a business website for a brand new wedding decor & events company, Lirovel. We have just established our logo and would love to use this logo on the website.

Because this is a new business venture, we do not have too many pictures to post online. It'd be exciting what your creativity can bring us!

Our website is: www.Lirovel.ca

Target Market(s)

Our clientele demographic is targeted to brides and bridesmaids in their 20-30 years old.

Industry/Entity Type

Wedding

Requirements
Must have
• - Professional, elegant and artistic look
- Modern feeling
- Very catchy flash intro page
- Ability to show Chatterleaf posts
Nice to have
• - Easy to navigate, crisp and clean
- Live pingvox messaging or online messaging

I would like to have navigation pages like: Lirovel Brand, Collections, Features, Contact Us, etc.

Each page I want it to be clean and easy to read. Something like the following website: http://www.brenquavi.com/

We offer:
BACKDROPS
HEAD, CAKE & RECEIVING TABLES DECOR
CHAIRCOVERS
TABLE CLOTHS & OVERLAYS
NAPKINS
CENTREPIECES
CEREMONY SET-UP
CANDELABRA
CRYSTAL GLOBES
LED LIGHTING
CUSTOM DESIGN AISLE RUNNERS
CAKE STANDS
MONEY BOX
CHARGERS
GOBO LIGHTING
Should not have
• - traditional, old style website
- very static (dull)
- too many images or busy layout
- no "standardized" website templates such as: www.zintep.com/gallery/weddings

```html
<!DOCTYPE html>
<html lang="en">
<head>
<meta charset="utf-8">
<title>Lirovel — Wedding Decor and Events</title>
<link rel="stylesheet" href="https://fonts.googleapis.com/css2?family=Dosis:wght@400;500&family=Great+Vibes&family=Open+Sans:wght@400&display=swap">
<style>
  :root {
    --pink: #e0197f;
    --pink-soft: #e8449a;
    --pink-dark: #b5106a;
    --grey-text: #6b6b6b;
    --grey-nav: #777777;
    --header-bg: #fbfbf8;
    --stage-bg: #eceae5;
    --footer-bg: #ffffff;
    --icon-grey: #c9c9c9;
  }
  * { margin: 0; padding: 0; box-sizing: border-box; }
  html, body { width: 1200px; height: 850px; overflow: hidden; }
  body { position: relative; background: var(--stage-bg); font-family: 'Dosis', sans-serif; }

  .site-header {
    position: absolute; left: 0; top: 0; width: 1200px; height: 143px;
    background: var(--header-bg);
    box-shadow: 0 6px 10px -6px rgba(0,0,0,0.18);
    z-index: 2;
  }
  .brand-mark {
    position: absolute; left: 497px; top: 62px; width: 220px;
    display: flex; align-items: center; justify-content: center; gap: 10px;
  }
  .brand-mark .dot { width: 22px; height: 22px; border-radius: 50%; background: var(--pink); flex: none; }
  .brand-mark .name { font-family: 'Dosis', sans-serif; font-weight: 500; font-size: 50px; color: var(--grey-text); line-height: 1; }

  .main-nav a {
    position: absolute; top: 92px; font-size: 18px; letter-spacing: 1px;
    color: var(--grey-nav); text-decoration: none; text-transform: uppercase; font-weight: 400;
  }
  .main-nav a.active { color: var(--pink); }

  .social { position: absolute; display: flex; gap: 4px; }
  .social span { width: 28px; height: 28px; border-radius: 50%; background: var(--icon-grey); display: block; }
  .social--top { left: 926px; top: 8px; }
  .social--footer { left: 722px; top: 793px; }

  .intro-kicker {
    position: absolute; left: 0; top: 184px; width: 1200px; text-align: center;
    font-family: 'Great Vibes', cursive; font-size: 30px; color: #444;
  }
  .intro-title {
    position: absolute; left: 0; top: 218px; width: 1200px; text-align: center;
    font-family: 'Dosis', sans-serif; font-weight: 500; font-size: 56px; letter-spacing: 2px;
    color: var(--pink); line-height: 1;
  }

  .stripe-line {
    position: absolute; left: 0; top: 492px; width: 1200px; height: 6px;
    background: repeating-linear-gradient(135deg, var(--pink) 0 3px, #f3a6cc 3px 5px);
  }

  .slide { position: absolute; }
  .slide--left { left: 172px; top: 322px; width: 269px; height: 340px;
    background: linear-gradient(160deg, #9a6fe0 0%, #7a3fc8 45%, #4c2c7a 100%); }
  .slide--center { left: 441px; top: 301px; width: 318px; height: 344px; z-index: 1;
    background: linear-gradient(180deg, #d9d6dd 0%, #8e8a92 45%, #6d6a70 75%, #d8d8d8 100%);
    box-shadow: 0 0 12px rgba(0,0,0,0.25); }
  .slide--right { left: 759px; top: 322px; width: 270px; height: 340px;
    background: linear-gradient(180deg, #6a5a7a 0%, #b9a6d8 40%, #a58fb6 70%, #9b8590 100%); }

  .ribbon { position: absolute; z-index: 2; }
  .ribbon text { font-family: 'Dosis', sans-serif; font-size: 21px; letter-spacing: 1.5px; fill: #fff; }

  .slider-arrow { position: absolute; top: 465px; z-index: 3; }
  .slider-arrow--prev { left: 166px; }
  .slider-arrow--next { left: 1004px; }

  .stage-shadow {
    position: absolute; left: 200px; top: 716px; width: 800px; height: 12px;
    border-radius: 50%; background: radial-gradient(ellipse at center, rgba(0,0,0,0.35) 0%, rgba(0,0,0,0) 70%);
  }

  .site-footer { position: absolute; left: 0; top: 746px; width: 1200px; height: 104px; background: var(--footer-bg); }
  .footer-nav { position: absolute; left: 171px; top: 38px; font-family: 'Open Sans', sans-serif; font-size: 11px; color: #555; }
  .footer-nav a { color: #555; text-decoration: none; }
  .footer-nav .sep { margin: 0 5px; }
  .copyright { position: absolute; left: 167px; top: 62px; font-family: 'Open Sans', sans-serif; font-size: 10.5px; color: #555; }
  .footer-mark {
    position: absolute; left: 862px; top: 38px; display: flex; align-items: center; gap: 8px;
  }
  .footer-mark .dot { width: 16px; height: 16px; border-radius: 50%; background: var(--pink); }
  .footer-mark .name { font-weight: 500; font-size: 38px; color: var(--grey-text); line-height: 1; }
</style>
</head>
<body>

<header class="site-header">
  <nav class="main-nav">
    <a class="active" href="#" style="left:189px">The Brand</a>
    <a href="#" style="left:299px">Collection</a>
    <a href="#" style="left:411px">Press</a>
    <a href="#" style="left:752px">Features</a>
    <a href="#" style="left:850px">Contact</a>
    <a href="#" style="left:933px">Shop Online</a>
  </nav>
  <div class="brand-mark"><span class="dot"></span><span class="name">Lirovel</span></div>
  <div class="social social--top" aria-label="Social links"><span></span><span></span><span></span></div>
</header>

<p class="intro-kicker">Brand New</p>
<h1 class="intro-title">WEDDING DECOR AND EVENTS COMPANY</h1>

<div class="stripe-line"></div>

<div class="slide slide--left" role="img" aria-label="Receiving tables with draped satin covers under purple uplighting"></div>
<div class="slide slide--center" role="img" aria-label="Banquet hall with white chairs, grey table cloths and pink runners under draped backdrops"></div>
<div class="slide slide--right" role="img" aria-label="Reception hall with chandeliers, ceiling drapes and covered chairs in lavender light"></div>

<svg class="ribbon" style="left:147px;top:662px" width="299" height="42" viewBox="0 0 299 42">
  <polygon points="0,0 299,0 299,42 0,42 14,21" fill="var(--pink)"/>
  <text x="159" y="29" text-anchor="middle">RECEIVING TABLES DECOR</text>
</svg>
<svg class="ribbon" style="left:432px;top:645px" width="332" height="54" viewBox="0 0 332 54">
  <rect x="0" y="0" width="332" height="54" fill="var(--pink-soft)"/>
  <text x="166" y="33" text-anchor="middle">TABLE CLOTHS AND OVERLAYS</text>
</svg>
<svg class="ribbon" style="left:751px;top:662px" width="297" height="42" viewBox="0 0 297 42">
  <polygon points="0,0 297,0 283,21 297,42 0,42" fill="var(--pink)"/>
  <text x="140" y="29" text-anchor="middle">RECEIVING TABLES DECOR</text>
</svg>

<svg class="slider-arrow slider-arrow--prev" width="30" height="64" viewBox="0 0 30 64" aria-label="Previous">
  <path d="M30,0 L30,64 L14,64 Q0,64 0,50 L0,14 Q0,0 14,0 Z" fill="var(--pink)"/>
  <path d="M18,25 L12,32 L18,39" stroke="#fff" stroke-width="3" fill="none" stroke-linecap="round"/>
</svg>
<svg class="slider-arrow slider-arrow--next" width="30" height="64" viewBox="0 0 30 64" aria-label="Next">
  <path d="M0,0 L0,64 L16,64 Q30,64 30,50 L30,14 Q30,0 16,0 Z" fill="var(--pink)"/>
  <path d="M12,25 L18,32 L12,39" stroke="#fff" stroke-width="3" fill="none" stroke-linecap="round"/>
</svg>

<div class="stage-shadow"></div>

<footer class="site-footer">
  <nav class="footer-nav">
    <a href="#">Lirovel Brand</a><span class="sep">|</span><a href="#">Collections</a><span class="sep">|</span><a href="#">Features</a><span class="sep">|</span><a href="#">Contact Us</a>
  </nav>
  <p class="copyright">© 2013 | Lirovel All rights reserved</p>
  <div class="footer-mark"><span class="dot"></span><span class="name">Lirovel</span></div>
</footer>
<div class="social social--footer" aria-label="Social links"><span></span><span></span><span></span></div>

</body>
</html>
```